Gordon Pellbrook Consulting - Web Design Project

We need a web design for my new edgy consulting business specializing in innovation, technology and strategy.

It is our personal goal to turn each client into raving fans by helping them achieve their own business goals and aspirations through assisting them in raising their own innovation and marketing standards.

We provide our personalised and state-of-the-art services to our clients and boards who represent some of the world greatest innovative thinkers.
Updates

Here is some other information which may help shape your thinking.

I've had direct Involvement in the development of the following iPad, iPhone Applications and websites

FarbeyondOzlands.com (TerraLink platform) by Voyage Bureau
http://farbeyondozlands.example.au

Sail Verve by Bright Voyaging
https://apps.example-store.com/au/app/sail-verve/id100000001

uRedlandTR by Travel Territory Board
https://apps.example-store.com/au/app/uredlandtr/id100000002

Wexmoor Trips
http://www.wexmoortrips.example.au

Trek Mapper by Voyage Bureau
http://apps.example-store.com/au/app/trek-mapper/id100000003

Sunward by Sunward Travel Office
https://apps.example-store.com/au/app/sunward/id100000004

Upper Fernridge Valley Route by Visit Coastlands
https://apps.example-store.com/au/app/upper-fernridge-valley-route/id100000005

Wanderer Path by Travel Territory Board and Southern Plains Travel Council
https://apps.example-store.com/au/app/wanderers-path-grand-journey/id100000006

Gordon Pellbrook Consulting (GPC)
November 2012 – Present (8 months)Brisbane, Sydney, Canberra

Gordon’s consults to Small-to-Medium Enterprises (SME) and Government organisations on business strategy, technology strategy, risk mitigation, disruptive technology and innovation in the workplace.

Gordon’s consultancy mantra is that we cannot divorce economic life from cultural life particularly in an era when social capital may be as important as physical capital in business.

Reason: request from designers, I want to see their best efforts

Target Market(s)

35+

Industry/Entity Type

Business

Requirements
Must have
• Please use some of the personal image(s) contained in the zip files which can be downloaded from here

http://filedrop.example/k9Xq2Lm
http://filedrop.example/p4Rt7Vn
http://filedrop.example/z8Hw3Bc
Nice to have
• Black, Sleek design, maybe minimalist. Nice to have a Pixelle for the design. Nice to have it easily ported to Wordpress or be a modified Wordpress template. HTML 5, responsive design

```html
<!DOCTYPE html>
<html lang="en">
<head>
<meta charset="utf-8">
<title>Gordon Pellbrook Consulting</title>
<link rel="stylesheet" href="https://fonts.googleapis.com/css2?family=Open+Sans:ital,wght@0,300;0,400;0,600;0,700;1,300;1,400&display=swap">
<style>
  :root{
    --bg-dark:#242424;
    --bg-footer:#1b1b1b;
    --paper:#ffffff;
    --ink:#2b2b2b;
    --muted:#666666;
    --soft:#8a8a8a;
    --line:#d9d9d9;
    --coral:#f2625c;
    --tag:#c4403f;
    --nav:#8e8e8e;
    --light:#e8e8e8;
  }
  *{margin:0;padding:0;box-sizing:border-box}
  html,body{width:720px;height:1200px;overflow:hidden;background:var(--paper)}
  body{font-family:"Open Sans",Arial,sans-serif;color:var(--ink);position:relative}
  .abs{position:absolute}

  /* header + hero */
  .hero{position:absolute;left:0;top:0;width:720px;height:470px;background:radial-gradient(ellipse at 60% 40%,#303030 0%,var(--bg-dark) 60%,#1f1f1f 100%)}
  .brand{left:73px;top:20px;width:190px;height:29px;border:1px dotted #8a8a8a;color:#fff;font-size:13px;font-weight:600;line-height:27px;text-align:center}
  .main-nav{left:362px;top:33px;display:flex;font-size:7px;font-weight:700;color:var(--nav)}
  .main-nav a{color:inherit;text-decoration:none;padding:0 6px;border-left:1px dotted #666;line-height:10px}
  .main-nav a:first-child{border-left:none;padding-left:8px;color:#fff}
  .main-nav a:last-child{border-right:1px dotted #666}
  .header-rule{left:64px;top:72px;width:593px;border-top:1px dotted #6a6a6a}
  .nav-active{left:362px;top:71px;width:39px;height:2px;background:#fff}
  .slide-tag{left:64px;top:195px;width:97px;height:18px;background:var(--tag);color:#fff;font-size:8px;line-height:18px;text-align:center;border-radius:2px}
  .slide-title{left:64px;top:222px;font-size:21px;font-weight:400;color:#fff}
  .slide-lead{left:64px;top:258px;width:280px;font-size:11.5px;line-height:14px;color:#fff}
  .slide-text{left:64px;top:300px;width:300px;font-size:8.3px;line-height:15px;color:#9a9a9a}
  .slide-media{left:285px;top:92px;width:375px;height:320px}
  .slider-dot{top:421px;width:20px;height:20px;border-radius:50%;background:#2e2e2e;border:1px solid #3a3a3a}

  /* services */
  .service{top:478px;width:200px;text-align:center}
  .service h2{font-size:20px;font-weight:300;line-height:25px;color:var(--ink);margin-top:10px}
  .service .lead{font-size:12px;line-height:18px;color:var(--muted);margin-top:11px}
  .service .body{font-size:8.4px;line-height:14px;color:var(--muted);margin-top:8px}
  .service-icon{display:block;margin:0 auto}
  .section-rule{left:64px;top:730px;width:592px;border-top:1px dotted #999}

  /* about */
  .portrait{left:70px;top:755px;width:112px;height:112px;border-radius:50%;border:4px solid #fff;box-shadow:0 3px 8px rgba(0,0,0,.35);background:linear-gradient(160deg,#c9cbcd,#8a97a4 60%,#5e6b78)}
  .about-title{left:199px;top:753px;font-size:21px;font-weight:300;color:var(--ink)}
  .about-quote{left:199px;top:790px;width:255px;font-size:8.3px;line-height:14px;color:var(--muted)}
  .articles-head{left:473px;top:751px;width:181px;height:25px;background:var(--coral);color:#fff;font-size:20px;font-weight:300;line-height:25px;text-align:center}
  .article{left:473px;width:180px;padding-left:16px;font-size:8.3px;line-height:14px;color:var(--muted)}
  .article::before{content:"\2190";position:absolute;left:2px;top:0;color:#aaa;font-size:9px}
  .article-rule{left:473px;width:180px;border-top:1px solid var(--line)}
  .connect-title{left:64px;top:897px;font-size:20px;font-weight:300}
  .social{top:933px;width:27px;height:27px;border-radius:50%;border:2px solid #e1e1e1;box-shadow:0 1px 2px rgba(0,0,0,.3)}
  .tweet-title{left:256px;top:898px;font-size:20px;font-weight:300}
  .tweet-mark{left:383px;top:904px;width:18px;height:18px;border-radius:50%;background:#8ec9e8}
  .tweet-text{left:260px;top:930px;width:180px;font-size:8.3px;line-height:14px;color:var(--muted)}
  .tweet-author{left:260px;top:958px;width:177px;text-align:right;font-size:8.3px;color:var(--muted)}

  /* footer */
  .footer{position:absolute;left:0;top:997px;width:720px;height:203px;background:var(--bg-footer)}
  .testimonials-title{left:322px;top:1011px;font-size:22px;font-weight:400;color:#fff}
  .testimonial{left:100px;top:1054px;width:520px;text-align:center;font-size:12px;font-style:italic;font-weight:300;line-height:19px;color:#d0d0d0}
  .footer-nav{left:0;top:1109px;width:720px;text-align:center;font-size:7px;font-weight:700;color:#8a8a8a}
  .footer-nav span{margin:0 5px}
  .footer-nav .dot{color:#666}
  .copyright{left:0;top:1126px;width:720px;text-align:center;font-size:7px;font-weight:600;color:#777}
  .footer-brand{left:286px;top:1153px;width:153px;height:27px;border:1px solid #2e2e2e;color:#4a4a4a;font-size:11px;line-height:25px;text-align:center}
  .back-top{left:608px;top:1162px;font-size:7px;font-weight:700;color:#fff}
</style>
</head>
<body>

<header class="hero">
  <div class="abs brand">Gordon Pellbrook Consulting</div>
  <nav class="abs main-nav">
    <a href="#">Home</a><a href="#">About Us</a><a href="#">Innovation</a><a href="#">Technology</a><a href="#">Strategy</a><a href="#">Risk Mitigation</a>
  </nav>
  <div class="abs header-rule"></div>
  <div class="abs nav-active"></div>

  <span class="abs slide-tag">De Finibus Bonorum</span>
  <h1 class="abs slide-title">Sed ut perspiciatis</h1>
  <p class="abs slide-lead">sed do eiusmod tempor incididunt ut labore et dolore magna aliqua eiusmod tempor ut labore</p>
  <p class="abs slide-text">voluptatem accusantium doloremque laudantium, totam rem aperiam, eaque ipsa quae ab illo inventore veritatis et quasi architecto beatae vitae dicta sunt explicabo. voluptatem accusantium doloremque laudantium, totam rem aperiam, eaque ipsa quae ab illo inventore verita.</p>

  <svg class="abs slide-media" viewBox="0 0 375 320" role="img" aria-label="Photo of a smartphone showing a travel app with a canyon landscape">
    <defs>
      <linearGradient id="mediaShade" x1="0" y1="0" x2="1" y2="1">
        <stop offset="0" stop-color="#3a3a3a"/>
        <stop offset="0.5" stop-color="#1c1c1c"/>
        <stop offset="1" stop-color="#0f0f0f"/>
      </linearGradient>
      <linearGradient id="screenTone" x1="0" y1="0" x2="0" y2="1">
        <stop offset="0" stop-color="#8a6a88"/>
        <stop offset="0.5" stop-color="#b2552a"/>
        <stop offset="1" stop-color="#6a2a10"/>
      </linearGradient>
    </defs>
    <path d="M70 40 L300 0 L370 250 L120 318 Z" fill="url(#mediaShade)"/>
    <path d="M110 80 L285 45 L335 235 L160 280 Z" fill="url(#screenTone)" opacity=".85"/>
  </svg>

  <span class="abs slider-dot" style="left:337px"></span>
  <span class="abs slider-dot" style="left:366px"></span>
</header>

<section>
  <div class="abs service" style="left:62px">
    <svg class="service-icon" width="62" height="62" viewBox="0 0 62 62" aria-hidden="true">
      <circle cx="31" cy="31" r="29" fill="none" stroke="var(--coral)" stroke-width="2"/>
      <circle cx="31" cy="24" r="8" fill="var(--coral)"/>
      <path d="M17 45 Q18 34 31 34 Q44 34 45 45 Z" fill="var(--coral)"/>
    </svg>
    <h2>Small-to-Medium<br>Enterprises</h2>
    <p class="lead">eiusmod tempor incididunt ut labore et dolore magna aliqua.</p>
    <p class="body">Lorem ipsum dolor sit amet, consectetur adipisicing elit, sed do eiusmod tempor incididunt ut labore et dolore magna</p>
  </div>
  <div class="abs service" style="left:264px">
    <svg class="service-icon" width="62" height="62" viewBox="0 0 62 62" aria-hidden="true">
      <circle cx="31" cy="31" r="29" fill="none" stroke="var(--coral)" stroke-width="2"/>
      <path d="M31 17 A10 10 0 0 1 37 35 L36 41 L26 41 L25 35 A10 10 0 0 1 31 17 Z" fill="none" stroke="var(--coral)" stroke-width="2"/>
      <path d="M27 44 H35 M28 47 H34" stroke="var(--coral)" stroke-width="2"/>
      <path d="M31 11 V14 M19 16 L21 18 M43 16 L41 18 M15 27 H18 M44 27 H47" stroke="var(--coral)" stroke-width="1.5"/>
    </svg>
    <h2>Innovation<br>in the workplace</h2>
    <p class="lead">eiusmod tempor incididunt ut labore et dolore magna aliqua.</p>
    <p class="body">Lorem ipsum dolor sit amet, consectetur adipisicing elit, sed do eiusmod tempor incididunt ut labore et dolore magna</p>
  </div>
  <div class="abs service" style="left:465px">
    <svg class="service-icon" width="62" height="62" viewBox="0 0 62 62" aria-hidden="true">
      <circle cx="31" cy="31" r="29" fill="none" stroke="var(--coral)" stroke-width="2"/>
      <rect x="17" y="20" width="28" height="22" fill="var(--coral)"/>
      <path d="M19 39 L27 31 L32 35 L41 25" fill="none" stroke="#fff" stroke-width="2.5"/>
      <path d="M36 24 H43 V31" fill="none" stroke="#fff" stroke-width="2.5"/>
    </svg>
    <h2>Our Mantra<br>Duis aute irure</h2>
    <p class="lead">eiusmod tempor incididunt ut labore et dolore magna aliqua.</p>
    <p class="body">Lorem ipsum dolor sit amet, consectetur adipisicing elit, sed do eiusmod tempor incididunt ut labore et dolore magna</p>
  </div>
  <div class="abs section-rule"></div>
</section>

<section>
  <div class="abs portrait" role="img" aria-label="Portrait photo of Gordon Pellbrook"></div>
  <h2 class="abs about-title">Voluptatum deleniti</h2>
  <p class="abs about-quote">"Sed ut perspiciatis unde Nemo enim ipsam voluptatem, omnis iste natus error sit voluptatem accusantium doloremque laudantium, Nemo enim ipsam voluptatem, totam rem aperiam, eaque ipsa quae ab illo inventore veritatis et quasi architecto beatae vitae dicta sunt explicabo."</p>

  <h3 class="abs articles-head">Popular Articles</h3>
  <p class="abs article" style="top:787px">doloremque laudantium, totam rem aperiam, eaque ipsa quae ab illo inventore veritatis et</p>
  <div class="abs article-rule" style="top:835px"></div>
  <p class="abs article" style="top:842px">doloremque laudantium, totam rem aperiam, eaque ipsa quae ab illo inventore veritatis et</p>
  <div class="abs article-rule" style="top:889px"></div>
  <p class="abs article" style="top:898px">doloremque laudantium, totam rem aperiam, eaque ipsa quae ab illo inventore veritatis et Nemo enim ipsam voluptatem quia doloremque laudantium doloremque laudantium</p>

  <h3 class="abs connect-title">Connect With Me</h3>
  <span class="abs social" style="left:65px;background:#3b5998" aria-label="Social profile one"></span>
  <span class="abs social" style="left:98px;background:#29a9e1" aria-label="Social profile two"></span>
  <span class="abs social" style="left:132px;background:#d34836" aria-label="Social profile three"></span>
  <span class="abs social" style="left:165px;background:#c4302b" aria-label="Social profile four"></span>

  <h3 class="abs tweet-title">Latest Tweet</h3>
  <span class="abs tweet-mark" aria-hidden="true"></span>
  <p class="abs tweet-text">“ Sed ut perspiciatis unde omnis iste natus error sit voluptatem accusantium... ”</p>
  <p class="abs tweet-author">- Marlon Teece</p>
</section>

<footer class="footer"></footer>
<svg class="abs" style="left:284px;top:1011px" width="30" height="30" viewBox="0 0 30 30" aria-hidden="true">
  <rect x="2" y="5" width="21" height="22" rx="3" fill="none" stroke="#fff" stroke-width="2.5"/>
  <path d="M12 20 L14 14 L25 3 L28 6 L17 17 Z" fill="#fff"/>
</svg>
<h2 class="abs testimonials-title">Testimonials</h2>
<p class="abs testimonial">"At vero eos et accusamus et iusto odio dignissimos ducimus qui blanditiis praesentium voluptatum deleniti atque corrupti quos dolores et quas molestias “</p>
<nav class="abs footer-nav">
  <span>Home</span><span class="dot">•</span><span>About Us</span><span class="dot">•</span><span>Innovation</span><span class="dot">•</span><span>Technology</span><span class="dot">•</span><span>Strategy</span><span class="dot">•</span><span>Risk Mitigation</span>
</nav>
<p class="abs copyright">© 2013 Gordon Pellbrook Consulting (GPC). All rights reserved. Patents pending. Privacy Policy | Terms | Site Map</p>
<div class="abs footer-brand">Gordon Pellbrook Consulting</div>
<a class="abs back-top">Back to top <svg width="8" height="9" viewBox="0 0 8 9" aria-hidden="true"><path d="M4 0 L8 4 H5 V9 H3 V4 H0 Z" fill="#fff"/></svg></a>

</body>
</html>
```